Business broker needs designs for business card, letterhead and email signature

I require the following items:
- business cards
- letterhead
- email signature

My company is a Business Broker company that specialises in business sales across various industries. The company has branches in four areas and each area has its own logo and website. Initially for the submission I am happy to inspect 1 design and 1 layout for quillharborgroup but the winner will need to complete a design for each area.

The four areas are:
1. quillharborgroup
2. tealridgefuelsales
3. orbvalechainsales
4. pondgrovegrocerdeals

I would like one design for each of the above items for each area. In each design, there should be one prominent logo and then the remaining three should also be included, for eg, the letterhead for the quillharborgrp area would have the quillharborgrp logo featuring prominently, somewhere at the top perhaps and the logos of the other three areas would be smaller and perhaps at the bottom, down the side, etc.

For the business cards, one prominent logo should feature on one side with the remaining three logos on the reverse.

The overall objective is for each item to look like it belongs to one family . I need all the source files as I may add new industries moving forward.

Target Market(s)

My company targets business minded people looking to increase wealth,. make an investment or migrate to Australia. People who busy and are looking for efficient and professional service in securing their next business venture.

Industry/Entity Type

Business

Font styles to use
Serif
Sans Serif

Requirements
Must have
• I want something professional and corporate looking, not something cartoony or playful. I am happy for you to be creative.

```html
<!DOCTYPE html>
<html lang="en">
<head>
<meta charset="utf-8">
<title>quillharborgroup stationery</title>
<link rel="stylesheet" href="https://fonts.googleapis.com/css2?family=Jost:wght@400;500&family=Roboto+Condensed:wght@700&display=swap">
<style>
  :root {
    --red: #c8102e;
    --navy: #2d3640;
    --orange: #f5a300;
    --teal: #2fbcb0;
    --green: #7dbb2a;
    --ghost: #f1f1f3;
    --text: #2a2a2a;
    --backdrop: #e6e7ea;
    --paper: #ffffff;
  }
  * { box-sizing: border-box; margin: 0; padding: 0; }
  html, body { width: 938px; height: 1200px; overflow: hidden; background: var(--backdrop); }
  body { position: relative; font-family: "Jost", sans-serif; color: var(--text); }

  .letterhead {
    position: absolute; left: 40px; top: 10px; width: 858px; height: 1180px;
    background: var(--paper); overflow: hidden;
  }
  .top-band { position: absolute; left: 0; top: 0; width: 100%; height: 12px; }
  .header-rule { position: absolute; left: 17px; right: 17px; top: 104px; height: 1px; background: var(--red); }

  .brand { display: flex; align-items: center; gap: 8px; white-space: nowrap; }
  .brand-mark { width: 28px; height: 28px; background: var(--red); flex: none; }
  .brand-name { font-family: "Roboto Condensed", sans-serif; font-weight: 700; color: var(--navy); letter-spacing: -0.3px; }
  .letterhead-brand { position: absolute; right: 42px; top: 50px; }
  .letterhead-brand .brand-name { font-size: 31px; }
  .letterhead-brand .brand-mark { width: 36px; height: 36px; }

  .ghost-circle { position: absolute; left: 35px; top: 810px; width: 260px; height: 260px; border-radius: 50%; background: var(--ghost); }

  .footer-rule { position: absolute; left: 17px; right: 17px; top: 1100px; height: 1px; background: var(--red); }
  .footer { position: absolute; left: 57px; top: 1112px; display: flex; font-size: 14.5px; line-height: 22px; }
  .footer-col { padding: 0 16px; border-left: 1px solid #cfcfcf; }
  .footer-col:first-child { padding-left: 0; border-left: none; padding-right: 16px; }
  .color-bar { position: absolute; left: 0; bottom: 0; width: 100%; height: 11px; display: flex; }
  .color-bar span { flex: 1; }
  .c-orange { background: var(--orange); } .c-teal { background: var(--teal); } .c-green { background: var(--green); }

  .card { position: absolute; width: 360px; height: 205px; background: var(--paper); border: 1px solid #e2e2e2; overflow: hidden; }
  .card-front { left: 440px; top: 475px; }
  .card-back { left: 440px; top: 725px; }
  .card .top-band { height: 9px; }
  .card .color-bar { height: 7px; }
  .card-brand { position: absolute; right: 22px; top: 26px; gap: 6px; }
  .card-brand .brand-mark { width: 20px; height: 20px; }
  .card-brand .brand-name { font-size: 20px; }
  .name-tab {
    position: absolute; left: 0; top: 88px; width: 180px; height: 34px; background: var(--red);
    clip-path: polygon(0 0, 100% 0, 95% 100%, 0 100%);
    color: #fff; font-size: 15px; line-height: 34px; text-align: right; padding-right: 22px;
  }
  .role { position: absolute; left: 188px; top: 98px; font-size: 9px; }
  .card-contacts { position: absolute; left: 18px; top: 140px; font-size: 8.5px; line-height: 12px; list-style: none; }
  .card-contacts li { display: flex; align-items: center; gap: 4px; }
  .card-contacts svg { width: 7px; height: 7px; fill: var(--red); flex: none; }
  .card-contacts .label { color: var(--red); margin-left: 10px; }

  .ghost-circle-small { position: absolute; left: 28px; top: 52px; width: 110px; height: 110px; border-radius: 50%; background: var(--ghost); }
  .sister-brands { position: absolute; right: 26px; top: 50px; display: flex; flex-direction: column; gap: 14px; align-items: flex-start; }
  .sister-brands .brand { gap: 6px; }
  .sister-brands .brand-mark { width: 17px; height: 17px; }
  .sister-brands .brand-name { font-size: 17px; line-height: 20px; }
  .m-orange { background: var(--orange); } .m-teal { background: var(--teal); } .m-green { background: var(--green); }
</style>
</head>
<body>
  <main class="letterhead">
    <svg class="top-band" viewBox="0 0 858 12" preserveAspectRatio="none" aria-hidden="true"><polygon points="0,0 858,0 852,12 0,12" fill="var(--red)"/></svg>
    <div class="brand letterhead-brand"><span class="brand-mark"></span><span class="brand-name">quillharborgroup</span></div>
    <div class="header-rule"></div>

    <div class="ghost-circle" aria-hidden="true"></div>

    <section class="card card-front" aria-label="Business card front">
      <svg class="top-band" viewBox="0 0 360 9" preserveAspectRatio="none" aria-hidden="true"><polygon points="0,0 360,0 356,9 0,9" fill="var(--red)"/></svg>
      <div class="brand card-brand"><span class="brand-mark"></span><span class="brand-name">quillharborgroup</span></div>
      <div class="name-tab">Your Name</div>
      <div class="role">Founder</div>
      <ul class="card-contacts">
        <li><svg viewBox="0 0 10 10"><path d="M2 0l2 2-1 2a6 6 0 003 3l2-1 2 2-2 2C4 10 0 6 0 2z"/></svg>1300 555 018 <span class="label">ACN :</span>&nbsp;512 384 207</li>
        <li><svg viewBox="0 0 10 10"><rect x="0" y="2" width="10" height="7"/></svg>info@quillharborgroup.com.au</li>
        <li><svg viewBox="0 0 10 10"><circle cx="5" cy="5" r="5"/></svg>www.quillharborgroup.com.au</li>
        <li><svg viewBox="0 0 10 10"><path d="M5 0a4 4 0 014 4c0 3-4 6-4 6S1 7 1 4a4 4 0 014-4z"/></svg>Level 12, Harbor Point Tower, 18 Quill Lane, Sydney NSW 2000</li>
      </ul>
      <div class="color-bar"><span class="c-orange"></span><span class="c-teal"></span><span class="c-green"></span></div>
    </section>

    <section class="card card-back" aria-label="Business card back">
      <svg class="top-band" viewBox="0 0 360 9" preserveAspectRatio="none" aria-hidden="true"><polygon points="0,0 360,0 356,9 0,9" fill="var(--red)"/></svg>
      <div class="ghost-circle-small" aria-hidden="true"></div>
      <div class="sister-brands">
        <div class="brand"><span class="brand-mark m-orange"></span><span class="brand-name">orbvalechainsales</span></div>
        <div class="brand"><span class="brand-mark m-teal"></span><span class="brand-name">tealridgefuelsales</span></div>
        <div class="brand"><span class="brand-mark m-green"></span><span class="brand-name">pondgrovegrocerdeals</span></div>
      </div>
      <div class="color-bar"><span class="c-orange"></span><span class="c-teal"></span><span class="c-green"></span></div>
    </section>

    <div class="footer-rule"></div>
    <footer class="footer">
      <div class="footer-col">Level 12, Harbor Point Tower,<br>18 Quill Lane, Sydney NSW 2000</div>
      <div class="footer-col">P : 1300 555 018<br>ACN: 512 384 207</div>
      <div class="footer-col">E : info@quillharborgroup.com.au<br>W : www.quillharborgroup.com.au</div>
    </footer>
    <div class="color-bar"><span class="c-orange"></span><span class="c-teal"></span><span class="c-green"></span></div>
  </main>
</body>
</html>
```